Candy Bar Desgin

We need a postcard desgin for my new company. I just started a Candy bar/buffet called Sweet Table By Mimi. My motto is Sweet Table by Mimi for the teeny treaty. I will be attending a bridal show where I can display my work so there will be brides there. So I want something to pop. Maybe can add vases filled with candy. Add 20% off an event you book for attending the bridal show. I want colors. Candy colors. My company also do chocolate fountain bars as well. My website to add is www.sweettablebymimi.example
Email sweettablebymimi@mailbox.example
Phone 555-014-2968

Target Market(s)

Brides

Industry/Entity Type

It Company

Requirements
Must have
• Must have my motto. And my contact information
Should not have
• No old style don't like times new roman. Use fun fonts

```html
<!DOCTYPE html>
<html lang="en">
<head>
<meta charset="utf-8">
<title>Sweet Table By Mimi – Postcard</title>
<link rel="stylesheet" href="https://fonts.googleapis.com/css2?family=Lobster+Two:ital,wght@1,400;1,700&family=Roboto:wght@700&display=swap">
<style>
  :root {
    --red: #e61e2b;
    --white: #ffffff;
    --card-top: #fbe0d6;
    --card-bottom: #f4c4b5;
    --stage: #ece8e4;
    --line: #8a7a76;
    --photo-pink: #e8a8c0;
    --photo-gold: #d8b070;
    --photo-cream: #f2dcc0;
    --photo-rose: #e59a9a;
  }
  * { margin: 0; padding: 0; box-sizing: border-box; }
  html, body { width: 1200px; height: 722px; overflow: hidden; background: var(--stage); }
  .canvas { position: relative; width: 1200px; height: 722px; }
  .postcard {
    position: absolute; top: 171px; width: 560px; height: 380px;
    background: linear-gradient(180deg, var(--card-top), var(--card-bottom));
    overflow: hidden; box-shadow: 0 6px 18px rgba(0,0,0,.18);
  }
  .postcard--back { left: 25px; }
  .postcard--front { left: 615px; }
  .header-band {
    position: absolute; top: 0; left: 0; width: 100%; height: 84px;
    background: var(--red); border-bottom: 4px solid var(--white);
    box-shadow: 0 4px 0 var(--red);
  }
  .brand-title {
    position: absolute; top: 26px; left: 0; width: 100%; text-align: center;
    font-family: "Lobster Two", cursive; font-style: italic; font-weight: 700;
    color: var(--white); font-size: 24px; line-height: 30px; letter-spacing: .5px;
  }
  .postcard--back .brand-title { font-size: 19px; }
  /* back side */
  .illustration-couple {
    position: absolute; left: 32px; top: 104px; width: 146px; height: 146px; border-radius: 50%;
    background: radial-gradient(circle, #f6efe8 0%, #e9d9cc 70%, #d9b98c 100%);
    border: 3px solid #e3c9a0;
  }
  .stamp-box {
    position: absolute; left: 414px; top: 104px; width: 92px; height: 92px;
    background: var(--white); border: 2px solid #9a9a9a;
  }
  .address-lines { position: absolute; left: 262px; top: 200px; width: 270px; }
  .address-lines span { display: block; height: 30px; border-bottom: 2px dashed var(--line); }
  .contact { position: absolute; left: 30px; top: 264px; font-family: "Roboto", Arial, sans-serif; font-weight: 700; color: var(--red); }
  .contact__phone { font-size: 30px; line-height: 36px; border-bottom: 3px solid var(--red); display: inline-block; padding-right: 4px; }
  .contact__line { font-size: 14px; line-height: 22px; border-bottom: 2px solid var(--red); width: max-content; }
  /* front side */
  .photo {
    position: absolute; border: 5px solid var(--white);
    box-shadow: 0 3px 8px rgba(0,0,0,.25);
  }
  .photo--buffet { left: 40px; top: 130px; width: 118px; height: 86px; transform: rotate(-3deg); background: linear-gradient(135deg, var(--photo-pink), #c98aa8); }
  .photo--cakepops { left: 48px; top: 232px; width: 120px; height: 78px; transform: rotate(-3deg); background: linear-gradient(135deg, var(--photo-rose), var(--photo-cream)); }
  .photo--candytable { left: 395px; top: 100px; width: 125px; height: 70px; transform: rotate(3deg); background: linear-gradient(135deg, var(--photo-cream), var(--photo-pink)); }
  .photo--fountain { left: 418px; top: 185px; width: 112px; height: 96px; transform: rotate(3deg); background: linear-gradient(135deg, #8a5a3a, var(--photo-gold)); }
  .coupon {
    position: absolute; left: 188px; top: 148px; width: 190px; height: 116px;
    background: var(--white); border: 2px solid var(--red); border-radius: 14px;
    outline: 2px solid var(--photo-rose); outline-offset: 4px;
    text-align: center; font-family: "Lobster Two", cursive; font-style: italic; color: var(--red);
    padding-top: 12px;
  }
  .coupon__amount { font-size: 40px; line-height: 44px; font-weight: 400; }
  .coupon__amount small { font-size: 18px; }
  .coupon__terms { font-size: 14px; line-height: 16px; margin-top: 6px; }
  .motto-band {
    position: absolute; left: 0; top: 318px; width: 100%; height: 48px;
    background: var(--red); border-top: 3px solid var(--white); border-bottom: 3px solid var(--white);
    outline: 4px solid var(--red);
    font-family: "Lobster Two", cursive; font-style: italic; font-weight: 700;
    color: var(--white); font-size: 21px; line-height: 42px; text-align: center;
  }
</style>
</head>
<body>
<main class="canvas">
  <section class="postcard postcard--back">
    <div class="header-band"></div>
    <div class="brand-title">Sweet Table By Mimi</div>
    <div class="stamp-box"></div>
    <div class="illustration-couple" role="img" aria-label="Illustration of a bride and groom in a decorative circle"></div>
    <div class="address-lines"><span></span><span></span><span></span></div>
    <div class="contact">
      <div class="contact__phone">555-014-2968</div>
      <div class="contact__line">www.sweettablebymimi.example</div>
      <div class="contact__line">sweettablebymimi@mailbox.example</div>
    </div>
  </section>

  <section class="postcard postcard--front">
    <div class="header-band"></div>
    <div class="brand-title">Sweet Table By Mimi</div>
    <div class="photo photo--buffet" role="img" aria-label="Photo of a pink candy buffet table"></div>
    <div class="photo photo--cakepops" role="img" aria-label="Photo of pink cake pops and treats"></div>
    <div class="photo photo--candytable" role="img" aria-label="Photo of a candy table display with vases"></div>
    <div class="photo photo--fountain" role="img" aria-label="Photo of a chocolate fountain with dipping treats"></div>
    <div class="coupon">
      <div class="coupon__amount">20% <small>OFF</small></div>
      <div class="coupon__terms">an event you book for<br>attending the bridal show</div>
    </div>
    <div class="motto-band">Sweet Table by Mimi for the teeny treaty</div>
  </section>
</main>
</body>
</html>
```